car site and logo design

I am looking for a clean website that is easy to navigate to view and post used cars for sale. The required tabs are [Buy - Sell - News - Care Tips - Finance - Insurance - FAQ]
motorlane.example has a great search tool on the landing page. New & Zip code are not required.
wexa autos has a nice simple results display, although I am open to other neat clean layouts.
Users can create an account or login using their pinloop accounts, and follow, like, comment on other users posted cars. sellers can be given ratings as well.
displaying car information should be neat and simple, showing the seller name which can be clicked on and takes the viewer to the seller page to view other cars for sale if any. included in the car information when viewing a specific car a bell curve showing the prices available for the same car being sold on the site, and the position of this particular car.
the care tips, finance and insurance pages will have rectangular boxes with sponsored ads by the related companies.
the logo should be a cartoon style mechanic character, with a slogan next to it [buying a ride?, selling a ride?, ride adive? Query Tobin ] - the site will be called querytobin.
Sell tab would include a quick post box where user inserts the vehicle VIN number and will open a page where user will just have to upload the remaining data such as mileage, color, etc.
this is basically what the site is about.

Target Market(s)

target market will be older generation looking to buy and sell a car, will require easy features, as well as younger crowd who are familiar with using extra features.

Industry/Entity Type

Finance

Requirements
Nice to have
• site should have a light sense of social media site where user has a profile photo, can view user's history and activity

```html
<!DOCTYPE html>
<html lang="en">
<head>
<meta charset="utf-8">
<title>QueryTobin – Buy and Sell Cars</title>
<link rel="stylesheet" href="https://fonts.googleapis.com/css2?family=Open+Sans:wght@400;600;700&family=Roboto+Condensed:wght@400;700&display=swap">
<style>
:root{
  --page-dark:#1f1f1f;
  --header-bg:#2b2b2b;
  --bar-bg:#3a3a3a;
  --tab-active:#4a4a4a;
  --accent:#2ec4e4;
  --logo-text:#d9d9d9;
  --panel:#ffffff;
  --panel-border:#dcdcdc;
  --field-border:#c9c9c9;
  --label:#333333;
  --heading:#2f2f2f;
  --button-dark:#6f6f6f;
  --footer-bg:#2a2a2a;
  --footer-text:#a9a9a9;
  --footer-head:#e6e6e6;
  --footer-line:#444444;
}
*{box-sizing:border-box;margin:0;padding:0}
html,body{width:1200px;height:1000px;overflow:hidden}
body{position:relative;background:var(--page-dark);font-family:"Open Sans",Arial,sans-serif;color:var(--label)}
.abs{position:absolute}

/* Header */
.site-header{position:absolute;left:0;top:53px;width:1200px;height:71px;background:var(--header-bg)}
.mascot{left:145px;top:64px;width:88px;height:104px;border-radius:40px 40px 24px 24px;background:linear-gradient(165deg,#e8c45a 0%,#3f7cb8 55%,#25568c 100%);z-index:3}
.brand-name{left:240px;top:72px;font-family:"Open Sans",Arial,sans-serif;font-weight:400;font-size:34px;line-height:40px;color:var(--logo-text);z-index:3;white-space:nowrap}
.account-bar{left:758px;top:54px;width:211px;height:28px;background:var(--bar-bg);display:flex;align-items:center;justify-content:center;font-size:10px;color:#e4e4e4;white-space:nowrap}
.account-bar span{padding:0 8px;border-left:1px solid #555;line-height:14px}
.account-bar span:first-child{border-left:none}
.main-nav{left:527px;top:98px;height:26px;width:443px}
.main-nav a{position:absolute;top:0;height:26px;line-height:26px;font-size:10px;color:var(--accent);text-decoration:none;text-align:center;white-space:nowrap}
.main-nav a.active{background:var(--tab-active);border-top:1px solid #5c5c5c}
.nav-sep{position:absolute;top:2px;width:1px;height:24px;background:#444}

/* Hero */
.hero-bg{left:0;top:124px;width:1200px;height:606px;background:radial-gradient(ellipse at 30% 80%,#1d5f86 0%,#173447 35%,#273842 60%,#3c525e 100%)}
.quote-panel{left:230px;top:124px;width:243px;height:275px;background:linear-gradient(#ffffff,#eeeeee);border:1px solid var(--panel-border)}
.quote-head{height:34px;background:#464646;color:var(--accent);font-size:14px;line-height:34px;padding-left:10px;position:relative}
.quote-head::after{content:"";position:absolute;left:16px;bottom:-6px;border:6px solid transparent;border-top-color:#464646;border-bottom:0}
.field-label{position:absolute;font-size:9.5px;font-weight:700;color:var(--label)}
.text-input,.select-box{position:absolute;background:#fff;border:1px solid var(--field-border);height:24px}
.select-box::after{content:"";position:absolute;right:8px;top:10px;border:4px solid transparent;border-top:5px solid #aaa;border-bottom:0}
.checkbox{position:absolute;width:12px;height:12px;border:1px solid #ccc;background:#f7f7f7}
.small-note{position:absolute;font-size:9px;color:#666}
.btn{position:absolute;background:linear-gradient(#a3a3a3,var(--button-dark));color:#fff;text-align:center;font-family:"Roboto Condensed",Arial,sans-serif;border-radius:2px}

.slider{left:480px;top:144px;width:489px;height:255px;background:linear-gradient(180deg,#8fb1cc 0%,#c5d3dc 40%,#b7ab98 70%,#8f8b83 100%)}
.slider-caption{left:622px;top:158px;font-family:"Roboto Condensed",Arial,sans-serif;font-size:21px;color:#fff;white-space:nowrap}
.slider-dots{left:918px;top:382px;display:flex;gap:3px}
.slider-dots i{display:block;width:7px;height:7px;background:#6a6a6a}
.slider-dots i.on{background:#e8e8e8}

/* Sponsored slots */
.sponsor-slot{top:408px;width:239px;height:94px}
.slot-one{left:230px;background:linear-gradient(180deg,#e2c43a 0%,#e2c43a 64%,#f4f4f4 64%,#f4f4f4 100%)}
.slot-two{left:480px;background:linear-gradient(180deg,#f4f4f4 0%,#ececec 70%,#c9272c 70%,#c9272c 86%,#f4f4f4 86%)}

.newsletter{left:731px;top:408px;width:238px;height:94px;background:#fff}
.newsletter h3{position:absolute;left:9px;top:8px;font-family:"Roboto Condensed",Arial,sans-serif;font-weight:400;font-size:13px;color:#222}
.newsletter .rule{position:absolute;left:0;top:31px;width:238px;height:4px;background:#eee}
.newsletter .envelope{position:absolute;left:8px;top:40px}
.newsletter .text-input{left:55px;top:40px;width:174px;height:22px;font-size:9px;color:#999;line-height:20px;padding-left:5px}

/* Search boxes */
.search-card{background:var(--panel);border:4px solid #eeeeee}
.search-card h2{position:absolute;left:13px;top:10px;font-weight:600;font-size:20px;color:var(--heading)}
.used-car{left:230px;top:512px;width:365px;height:192px}
.new-car{left:605px;top:512px;width:364px;height:192px}

/* Footer */
.footer{left:0;top:730px;width:1200px;height:210px;background:var(--footer-bg);color:var(--footer-text);font-size:9px}
.footer-nav{position:absolute;left:0;top:12px;width:1200px;text-align:center}
.footer-nav span{margin:0 12px}
.footer-rule{position:absolute;left:230px;top:35px;width:739px;height:1px;background:var(--footer-line)}
.footer-col h4{position:absolute;font-size:9.5px;font-weight:700;color:var(--footer-head)}
.footer-list{position:absolute;list-style:none;line-height:18px;white-space:nowrap}
.col-sep{position:absolute;top:40px;width:1px;height:125px;background:#383838}
</style>
</head>
<body>

<header class="site-header"></header>
<div class="abs mascot" role="img" aria-label="Cartoon mechanic mascot holding a wrench"></div>
<div class="abs brand-name">QueryTobin</div>

<div class="abs account-bar"><span>Sign In</span><span>Register</span><span>Manage Reservations</span></div>

<nav class="abs main-nav">
  <a class="active" style="left:0;width:56px">BUY</a>
  <a style="left:112px;width:40px">SELL</a>
  <span class="nav-sep" style="left:163px"></span>
  <a style="left:170px;width:40px">NEWS</a>
  <span class="nav-sep" style="left:220px"></span>
  <a style="left:230px;width:52px">FINANCE</a>
  <span class="nav-sep" style="left:301px"></span>
  <a style="left:306px;width:56px">INSURANCE</a>
  <span class="nav-sep" style="left:369px"></span>
  <a style="left:380px;width:34px">FAQ</a>
  <span class="nav-sep" style="left:442px"></span>
</nav>

<div class="abs hero-bg" role="img" aria-label="Dark concrete wall with a black sports car lit by blue neon"></div>

<section class="abs quote-panel">
  <div class="quote-head">Free Dealer Price Quote</div>
  <div class="field-label" style="left:10px;top:51px">Location</div>
  <div class="text-input" style="left:10px;top:67px;width:222px"></div>
  <div class="checkbox" style="left:10px;top:96px"></div>
  <div class="small-note" style="left:27px;top:96px">Return at different location</div>
  <div class="field-label" style="left:10px;top:129px">Select Make</div>
  <div class="select-box" style="left:10px;top:145px;width:216px"></div>
  <div class="field-label" style="left:10px;top:190px">Select Model</div>
  <div class="select-box" style="left:10px;top:206px;width:216px"></div>
  <div class="btn" style="left:10px;top:239px;width:95px;height:23px;line-height:23px;font-size:13px">Get a Quote</div>
</section>

<div class="abs slider" role="img" aria-label="Champagne hatchback sedan driving along a coastal road"></div>
<div class="abs slider-caption">Lorem ipsum dolor sit amet, consectetur</div>
<div class="abs slider-dots"><i></i><i class="on"></i><i></i><i></i></div>

<div class="abs sponsor-slot slot-one" role="img" aria-label="Sponsored advertisement for a compact sedan"></div>
<div class="abs sponsor-slot slot-two" role="img" aria-label="Sponsored advertisement for certified pre-owned financing"></div>

<section class="abs newsletter">
  <h3>Sign up for our newsletter</h3>
  <div class="rule"></div>
  <svg class="envelope" width="40" height="40" viewBox="0 0 40 40" aria-hidden="true">
    <rect x="2" y="8" width="36" height="26" rx="2" fill="#f2f2f2" stroke="#bdbdbd"/>
    <path d="M2 10 L20 24 L38 10" fill="none" stroke="#bdbdbd" stroke-width="1.5"/>
  </svg>
  <div class="text-input">Email Address</div>
  <div class="btn" style="left:55px;top:69px;width:62px;height:17px;line-height:17px;font-size:9px">SUBSCRIBE</div>
</section>

<section class="abs search-card used-car">
  <h2>Used Car</h2>
  <div class="field-label" style="left:7px;top:53px">Select Make</div>
  <div class="select-box" style="left:7px;top:69px;width:216px"></div>
  <div class="field-label" style="left:7px;top:102px">Select Model</div>
  <div class="select-box" style="left:7px;top:118px;width:216px"></div>
  <div class="btn" style="left:193px;top:159px;width:61px;height:17px;line-height:17px;font-size:10px">GO</div>
</section>

<section class="abs search-card new-car">
  <h2>Price a New Car</h2>
  <div class="field-label" style="left:12px;top:53px">Select Make</div>
  <div class="select-box" style="left:12px;top:69px;width:216px"></div>
  <div class="field-label" style="left:12px;top:102px">Select Model</div>
  <div class="select-box" style="left:12px;top:118px;width:216px"></div>
  <div class="btn" style="left:192px;top:159px;width:61px;height:17px;line-height:17px;font-size:10px">GO</div>
</section>

<footer class="abs footer">
  <nav class="footer-nav"><span>Home</span><span>Special Offers</span><span>Cars</span><span>Locations</span><span>About</span><span>Contact</span></nav>
  <div class="footer-rule"></div>

  <div class="footer-col">
    <h4 style="left:230px;top:46px">Car Types</h4>
    <ul class="footer-list" style="left:230px;top:67px"><li>Compact</li><li>Economy</li><li>Full Size</li><li>Hybrid</li><li>Intermediate</li><li>Luxury</li></ul>
    <ul class="footer-list" style="left:308px;top:67px"><li>Midsize</li><li>Minivan</li><li>Passenger Van</li><li>Premium</li><li>Standard</li><li>SUV</li></ul>
  </div>
  <div class="col-sep" style="left:400px"></div>

  <div class="footer-col">
    <h4 style="left:430px;top:46px">Car&nbsp; Europe</h4>
    <ul class="footer-list" style="left:430px;top:67px"><li>Amsterdam</li><li>Austria</li><li>Belgium</li><li>Cyprus</li><li>Denmark</li><li>Finland</li></ul>
    <ul class="footer-list" style="left:511px;top:67px"><li>Germany</li><li>Greece</li><li>Holland</li><li>Ireland</li><li>Dublin</li><li>Italy</li></ul>
    <ul class="footer-list" style="left:583px;top:67px"><li>Malta</li><li>Malaga</li><li>Netherlands</li><li>Poland</li><li>Portugal</li><li>Spain</li></ul>
    <ul class="footer-list" style="left:656px;top:67px"><li>Sweden</li><li>Switzerland</li><li>Turkey</li><li>Rome</li><li>United Kingdom</li><li>More locations</li></ul>
  </div>
  <div class="col-sep" style="left:748px"></div>

  <div class="footer-col">
    <h4 style="left:777px;top:46px">Car&nbsp; Worlwide</h4>
    <ul class="footer-list" style="left:777px;top:67px"><li>Argentina</li><li>Australia</li><li>Brazil</li><li>Canada</li><li>Caribbean</li><li>Costa Rica</li></ul>
    <ul class="footer-list" style="left:844px;top:67px"><li>Egypt</li><li>El Salvador</li><li>Fiji</li><li>Honduras</li><li>Malaysia</li><li>Mauritius</li></ul>
    <ul class="footer-list" style="left:910px;top:67px"><li>Mexico</li><li>Morocco</li><li>Namibia</li><li>New Zealand</li><li>Peru</li><li>More locations</li></ul>
  </div>
</footer>

</body>
</html>
```